Design for schnapps bottle label "El Sendero"

Hi! On a small land lot we are producing our own Italian schnapps "Grappa". For the bottles we would like to modernize our current labes that you find below. The two cats looking at each other should remain, but updated and more modern. I am very much looking forward to your suggestions. Best, Tobias

Target Market(s)

Schnapps bottle label

Requirements
Must have
• Cats should resemble the cats that are decorating the house entry (see attached), however, should have a more modern appearance.

Text elements should remain: "Grappa", "El Sendero", "Legnoso", "[Vintage Year], "Raccolta No", "Vol %"
Should not have
• Current ornament can be used, replaced or deleted (whatever looks best)

```html
<!DOCTYPE html>
<html lang="it">
<head>
<meta charset="utf-8">
<title>Grappa legnoso 2015 – El Sendero</title>
<link rel="stylesheet" href="https://fonts.googleapis.com/css2?family=Federant&family=Amarante&display=swap">
<style>
  :root {
    --backdrop: #e8e6e3;
    --label-light: #f7b54c;
    --label-mid: #f2a33a;
    --label-deep: #e8932a;
    --ink: #123f48;
  }
  html, body {
    margin: 0;
    padding: 0;
    width: 1200px;
    height: 960px;
    overflow: hidden;
    background: var(--backdrop);
  }
  .label {
    position: absolute;
    left: 340px;
    top: 40px;
    width: 520px;
    height: 880px;
    box-sizing: border-box;
    overflow: hidden;
    background: linear-gradient(160deg, var(--label-light) 0%, var(--label-mid) 55%, var(--label-deep) 100%);
    border-bottom: 12px solid var(--ink);
    color: var(--ink);
    font-family: "Amarante", serif;
  }
  .ornament {
    position: absolute;
    left: 190px;
    top: 68px;
    width: 260px;
    height: 34px;
  }
  .title {
    position: absolute;
    left: 0;
    right: 0;
    top: 118px;
    margin: 0;
    text-align: center;
    font-family: "Federant", serif;
    font-weight: 400;
    font-size: 124px;
    line-height: 1;
    letter-spacing: 0;
    white-space: nowrap;
  }
  .title-rule {
    position: absolute;
    left: 55px;
    top: 262px;
    width: 410px;
    height: 2px;
    background: var(--ink);
  }
  .variety {
    position: absolute;
    left: 0;
    right: 0;
    top: 328px;
    margin: 0;
    text-align: center;
    font-size: 46px;
    line-height: 1;
  }
  .connector {
    position: absolute;
    left: 0;
    right: 0;
    top: 412px;
    margin: 0;
    text-align: center;
    font-size: 46px;
    line-height: 1;
  }
  .cats {
    position: absolute;
    left: 90px;
    top: 474px;
    width: 340px;
    height: 190px;
  }
  .producer {
    position: absolute;
    left: 0;
    right: 0;
    top: 690px;
    margin: 0;
    text-align: center;
    font-size: 52px;
    letter-spacing: 3px;
    line-height: 1;
  }
  .details {
    position: absolute;
    left: 6px;
    right: 6px;
    top: 822px;
    display: flex;
    justify-content: space-between;
    font-size: 28px;
    line-height: 1;
  }
</style>
</head>
<body>
  <main class="label">
    <svg class="ornament" viewBox="0 0 260 34" role="img" aria-label="Decorative scroll ornament above the title">
      <rect x="0" y="0" width="260" height="34" rx="8" fill="#d9822a" opacity="0.45"/>
    </svg>
    <h1 class="title">Grappa</h1>
    <div class="title-rule"></div>
    <p class="variety">“legnoso” 2015</p>
    <p class="connector">di</p>
    <svg class="cats" viewBox="0 0 340 190" role="img" aria-label="Illustration of two stretching cats facing each other">
      <rect x="0" y="0" width="340" height="190" rx="16" fill="#2b5a5c" opacity="0.35"/>
    </svg>
    <p class="producer">El Sendero</p>
    <div class="details">
      <span class="batch">Raccolta No. 01</span>
      <span class="strength">41.0% Vol</span>
    </div>
  </main>
</body>
</html>
```